Your Health, Your Time, Your Way: Personalized, Concierge Care Elevated to Modern Medicine

We need to incorporate an image of our new doctor (Dr. Malvina Okoruwe, MD) with our office logo ( Harborline Family Clinic) and dialogue that shows how simple it is to schedule a free consult and learn what our office has to offer patients. The colors should be consistent with our website- the CMYK codes will be attached for your use below. The font should be easy to read. The text should be clear, and convey value to the patient for chosing us over anyone else ( we offer primary care, preventive medicine, urgen care and functional medicine with 24 hour direct access to care with some of our strengths including focus on individualized care, cutting edge medicine, blended functional and traditional style. We aim to transform lives through patient centered innovative and individualized care plan. I have attached a "mock" image but the details ( office address, name, phone number are incorrect) The correct info is Harborline Family Clinic 4187 Wrenfield Ave Suite 214, Clearwater, FL 33759 and phone number (727)482-3095. A possible hook could read: welcoming new patients now- Your Health, Your Time, Your Way: Personalized Care Meets Modern Medicine
Updates

I did not realize that there was a tab with more information to fill for the designers to see, or for me to upload the basic information they need to create the design.

Target Market(s)

Patients over 18 years of age with interest in longevity, functional and traditional medicine; the postcards will be mailed to our CURRENT patients, and they are a reminder of what we do, new patient availability AND a request for them to refer friends or families

Industry/Entity Type

medical

Font styles to use
Sans Serif

Colors

Designer to choose colors to be used in the design.

Requirements
Must have
• simple reminder to current patients of what we offer, and a call to action for our patients to refer friends and family for same level of excellence;consistency with brand ( see business card and cmyx codes for colors);photo of new physician; logo Harborline Family Clinic, web site (https://harborlinefamilyclinic.net); Must clearly express accepting new patients; simple to call/email to schedule free consultation;; include our email (office@harborlinefamilyclinic.org), phone number (727)482-3095; our address 4187 Wrenfield Ave Suite 214, Clearwater, FL 33759
Nice to have
• photo of our new physician ( in blue jacket: Dr. Malvina Okoruwe, MD) should not take up too much space
Should not have
• clutter, or close text; full sentences( bulleted text preferred)

```html
<!DOCTYPE html>
<html lang="en">
<head>
<meta charset="utf-8">
<title>Harborline Family Clinic – Welcoming Dr. Malvina Okoruwe</title>
<link href="https://fonts.googleapis.com/css2?family=Poppins:wght@400;500;600;700&display=swap" rel="stylesheet">
<style>
  :root {
    --navy: #0b3a8f;
    --band: #003189;
    --sky: #3d8fd1;
    --pale: #cfe3f5;
    --white: #ffffff;
    --ink: #1d1d1d;
    --photo-top: #4a3630;
    --photo-bottom: #1b2340;
    --group-top: #b9b7c0;
    --group-bottom: #e9e7ee;
  }
  * { margin: 0; padding: 0; box-sizing: border-box; }
  html, body { width: 1200px; height: 857px; overflow: hidden; background: var(--white); }
  .postcard {
    position: relative; width: 1200px; height: 857px; overflow: hidden;
    background: var(--white); font-family: "Poppins", sans-serif; color: var(--navy);
  }
  .band-accent { position: absolute; left: 0; top: 553px; width: 1200px; height: 18px; background: var(--sky); }
  .band { position: absolute; left: 0; top: 571px; width: 1200px; height: 286px; background: var(--band); }
  .doctor-portrait {
    position: absolute; left: 560px; top: 35px; width: 540px; height: 822px;
    border-radius: 270px 270px 0 0;
    background: linear-gradient(180deg, var(--photo-top) 0%, #7a5a4c 35%, var(--photo-bottom) 62%, var(--photo-bottom) 100%);
  }
  .brand-name {
    position: absolute; left: 1048px; top: 58px; width: 140px;
    font-size: 17px; line-height: 24px; font-weight: 500; color: var(--ink);
  }
  .eyebrow {
    position: absolute; left: 52px; top: 16px;
    font-size: 13px; font-weight: 600; letter-spacing: 1.5px; text-transform: uppercase; color: var(--sky);
  }
  .title {
    position: absolute; left: 52px; top: 38px;
    font-size: 44px; font-weight: 700; letter-spacing: -0.5px; line-height: 1.1;
  }
  .welcome { position: absolute; left: 52px; top: 102px; width: 470px; }
  .welcome-head { font-size: 17px; font-weight: 700; line-height: 23px; }
  .welcome-body { font-size: 16.5px; font-weight: 400; line-height: 23px; }
  .interests-head {
    position: absolute; left: 52px; top: 258px; width: 470px;
    font-size: 17px; font-weight: 700; line-height: 23px;
  }
  .interests {
    position: absolute; left: 52px; top: 312px; width: 400px;
    list-style: none; display: flex; flex-wrap: wrap; column-gap: 20px;
    font-size: 20px; font-weight: 500; line-height: 26px;
  }
  .interests li::before { content: "•"; margin-right: 10px; }
  .services { position: absolute; left: 52px; top: 380px; width: 285px; }
  .services-head { font-size: 15px; font-weight: 700; line-height: 22px; }
  .services-list { list-style: none; font-size: 14.5px; font-weight: 500; line-height: 21px; }
  .services-list li::before { content: "✓"; color: var(--sky); margin-right: 8px; font-weight: 700; }
  .team-photo {
    position: absolute; left: 346px; top: 361px; width: 328px; height: 328px;
    border-radius: 50%; border: 13px solid var(--sky);
    background: linear-gradient(180deg, var(--group-top) 0%, var(--group-bottom) 60%, #2a2a30 100%);
  }
  .cta { position: absolute; left: 32px; top: 586px; width: 300px; color: var(--white); }
  .cta-main { font-size: 19px; font-weight: 700; line-height: 25px; }
  .cta-sub { font-size: 14px; font-weight: 500; line-height: 20px; color: var(--pale); }
  .contact { position: absolute; left: 32px; color: var(--white); display: flex; gap: 14px; align-items: flex-start; }
  .contact-address { top: 660px; }
  .contact-address p { font-size: 22px; font-weight: 600; line-height: 28px; }
  .contact-phone { top: 756px; align-items: center; }
  .contact-phone p { font-size: 28px; font-weight: 600; line-height: 36px; }
  .contact-online {
    position: absolute; left: 32px; top: 808px; color: var(--pale);
    display: flex; gap: 18px; font-size: 14px; font-weight: 500; line-height: 20px;
  }
  .icon { flex: none; fill: var(--white); }
</style>
</head>
<body>
<main class="postcard">
  <div class="band-accent"></div>
  <div class="band"></div>

  <div class="doctor-portrait" role="img" aria-label="Portrait of Dr. Malvina Okoruwe smiling, wearing a navy blazer over a red top"></div>

  <div class="brand-name">Harborline<br>Family<br>Clinic</div>

  <p class="eyebrow">Welcoming new patients now</p>
  <h1 class="title">Harborline Family Clinic</h1>

  <section class="welcome">
    <p class="welcome-head">Welcomes Dr. Malvina Okoruwe</p>
    <p class="welcome-body">Cedar Point Family Medicine is pleased to welcome board certified family medicine practitioner, Dr. Malvina Okoruwe, to our team. Dr. Okoruwe shares our passion for providing high-quality, personalized care.</p>
  </section>

  <p class="interests-head">Dr. Okoruwe practices the full range of family medicine with special interests in:</p>
  <ul class="interests">
    <li>Women's Health</li>
    <li>Diabetes</li>
    <li>Obesity</li>
  </ul>

  <section class="services">
    <p class="services-head">We offer:</p>
    <ul class="services-list">
      <li>Primary &amp; Preventive Care</li>
      <li>Urgent Care</li>
      <li>Functional Medicine</li>
      <li>24-Hour Direct Access</li>
    </ul>
  </section>

  <div class="team-photo" role="img" aria-label="Group photo of Dr. Okoruwe with two clinic team members"></div>

  <div class="cta">
    <p class="cta-main">Call or email for a free consult</p>
    <p class="cta-sub">Refer friends &amp; family for the same care</p>
  </div>

  <div class="contact contact-address">
    <svg class="icon" width="22" height="31" viewBox="0 0 24 34" aria-hidden="true">
      <path d="M12 0C5.4 0 0 5.3 0 11.9 0 20 12 34 12 34s12-14 12-22.1C24 5.3 18.6 0 12 0zm0 16.5a4.6 4.6 0 1 1 0-9.2 4.6 4.6 0 0 1 0 9.2z"/>
    </svg>
    <p>Harborline Family Clinic<br>4187 Wrenfield Ave Suite 214,<br>Clearwater, FL 33759</p>
  </div>

  <div class="contact contact-phone">
    <svg class="icon" width="24" height="24" viewBox="0 0 32 32" aria-hidden="true">
      <path d="M8.6 2.5l3.6 5.8c.5.8.3 1.8-.4 2.4l-2.3 1.9c1.8 3.8 4.2 6.3 7.9 8.2l2-2.3c.6-.7 1.6-.9 2.4-.4l5.8 3.6c.9.5 1.2 1.6.7 2.5l-1.7 3c-.8 1.4-2.4 2.1-4 1.7C12.2 27 5 19.8 2.8 9.4c-.4-1.6.3-3.2 1.7-4l3-1.7c.4-.3.9-.1 1.1-.2z"/>
      <path d="M18 3.5a10.5 10.5 0 0 1 10.5 10.5h-2.6A7.9 7.9 0 0 0 18 6.1zm0 4.4a6.1 6.1 0 0 1 6.1 6.1h-2.6A3.5 3.5 0 0 0 18 10.5z"/>
    </svg>
    <p>(727)482-3095</p>
  </div>

  <div class="contact-online">
    <span>office@harborlinefamilyclinic.org</span>
    <span>harborlinefamilyclinic.net</span>
  </div>
</main>
</body>
</html>
```